Book/Ebook Cover design for teen girls on purity/modesty
The Shape of Stillness: A Young Woman's Map to Quiet Strength
Book/Ebook Cover design for teen girls on purity/modesty - Books
Creative Brief
This book will be marketed to teenage girls, female family members like moms, grandmothers, aunts, etc., youth pastors, pastors, etc. I want a clean, fresh yet feminine look and feel. I envision an ornate mirror (handheld or otherwise) with the word "purity" being reflected on the mirror from the title. That is what's in my mind but I'm open to other ideas. Colors I like: aqua blue, bright green, and white.
Books
Feminine, fresh, charming, clean, modern.
This book will be published through Inkvale Press and Pagebrook. Full Bleed needed for the hard copy book. No less that 300 DPI. Need to know the basics about trim, margin, etc for book covers. RGB preferred.
tmerrow tmerrow
To Designers, I've uploaded an updated bio for myself for the back cover. I'll be choosing a winner very soon! Thank you so much for all your designs and hard work. I really appreciate it! Colette
FRIENDLY NOTE TO ALL DESIGNERS! Thanks for all your designs so far. Please do not include images of girls. I want the cover to draw girls from all backgrounds and an image of a girl whose skin color, hair and clothing makes a statement to one particular kind of girl. I want to make a statement to as many different kinds of girls as possible as the message is for them all. Also author name should either read "Colette J. Merrow" or "Colette Merrow". That's all for now. Please let me know how else I can help.
To all designers, Thanks for your willingness to create a design for my book! Size of book is 5.5X8.5. I'll need front and back cover designed. The mirror idea (described in the brief) is just something in my head. It can be pulled off believe but I'm also open to whatever fresh, clean and modern ideas you may have! Thanks again, tmerrow
Hi designers, It was brought to my attention that possibly the reason I haven't been getting many designers to commit is because this project isn't marked "guaranteed". I was under the impression that all projects were guaranteed. I do intend on picking a winner! I will call CS first thing Monday to see if I can change the project to read that it indeed is guaranteed. Until then, thanks so much for your submissions! I'm looking forward to picking one of your designs!
Dear designers, I would like to see some minimalistic designs. Simplistic but charming and feminine with a modern touch. Maybe the background the aqua blue color I like with a cute sketch of a mirror in white or with "purity" in a script font of some sort in the mirror. I'm not sure I'm going to like any of the random background kind of pictures. Thanks so much everyone. Tmerrow
Designers, The text for the back cover has not also been uploaded. Thanks!
To all designers, Thanks ahead of time for taking time to work on this project! I'm super excited to see what you all come up with. Please don't hesitate to ask questions or make suggestions. I have uploaded my head shot to use for the back cover. I am putting the finishing touches on the text for the back cover as well and will have that uploaded tonight or tomorrow. I'm not sure about how the ISBN will be printed on the book. Getting details on that as well. Thanks again! tmerrow

```html
<!DOCTYPE html>
<html lang="en">
<head>
<meta charset="utf-8">
<title>The Shape of Stillness — Cover Spread</title>
<link href="https://fonts.googleapis.com/css2?family=Parisienne&family=Raleway:wght@400;600;700&family=Lora:ital,wght@0,400;1,400&display=swap" rel="stylesheet">
<style>
  :root{
    --aqua:#2cbcbd;
    --aqua-deep:#1a9fa3;
    --aqua-soft:#bfeceb;
    --paper:#ffffff;
    --ink:#4a4f55;
    --stage:#eef1f2;
    --silver-1:#e9f4f6;
    --silver-2:#9fc6cf;
  }
  *{margin:0;padding:0;box-sizing:border-box}
  html,body{width:1200px;height:718px;overflow:hidden;background:var(--stage)}
  .spread{
    position:absolute;left:153px;top:29px;width:894px;height:660px;
    display:flex;box-shadow:0 4px 18px rgba(0,0,0,.12);
  }
  .panel{position:relative;height:100%;background:var(--paper);overflow:hidden}
  .back{width:427px}
  .spine{width:40px;border-left:1px solid #e3e7e8;border-right:1px solid #e3e7e8}
  .front{width:427px}
  .band-top,.band-bottom{position:absolute;left:0;right:0;background:var(--aqua)}
  .band-top{top:0;height:10px}
  .band-bottom{bottom:0;height:44px}

  /* back cover */
  .back-title{
    position:absolute;top:22px;left:0;right:0;text-align:center;
    font-family:"Parisienne",cursive;color:var(--aqua);font-size:34px;
  }
  .blurb{
    position:absolute;top:76px;left:34px;right:34px;
    font-family:"Lora",serif;font-size:10.5px;line-height:1.55;color:var(--ink);text-align:justify;
  }
  .blurb::first-letter{font-size:22px;color:var(--aqua);float:left;line-height:1;margin-right:3px}
  .promise{
    position:absolute;top:262px;left:0;right:0;background:var(--aqua);
    padding:12px 34px 14px;color:var(--paper);font-family:"Raleway",sans-serif;
  }
  .promise h3{font-size:10px;font-weight:700;letter-spacing:1px;margin-bottom:6px}
  .promise ul{list-style:none;font-size:9.5px;line-height:1.6}
  .promise li::before{content:"•";margin-right:6px}
  .author-photo{
    position:absolute;top:412px;left:34px;width:92px;height:112px;
    background:linear-gradient(160deg,#d9e4e6,#8aa2a8);
  }
  .bio{position:absolute;top:410px;left:140px;right:34px;font-family:"Lora",serif;color:var(--ink)}
  .bio h4{font-family:"Raleway",sans-serif;font-size:11px;font-weight:700;letter-spacing:1px;color:var(--aqua-deep);margin-bottom:5px}
  .bio p{font-size:9.5px;line-height:1.5}

  /* spine */
  .spine-text{
    position:absolute;top:50%;left:50%;transform:translate(-50%,-50%) rotate(90deg);
    white-space:nowrap;display:flex;align-items:center;gap:60px;
  }
  .spine-title{font-family:"Parisienne",cursive;color:var(--aqua);font-size:22px}
  .spine-author{font-family:"Raleway",sans-serif;font-weight:600;font-size:11px;letter-spacing:2px;color:var(--aqua-deep)}

  /* front cover */
  .front-title{
    position:absolute;top:30px;left:0;right:0;text-align:center;
    font-family:"Parisienne",cursive;color:var(--aqua);line-height:.95;
  }
  .front-title .small{display:block;font-size:40px;margin-right:170px}
  .front-title .large{display:block;font-size:72px}
  .front-title .mid{display:block;font-size:38px}
  .mirror{
    position:absolute;top:250px;left:118px;width:190px;height:290px;
    border-radius:95px 95px 40px 40px;
    background:radial-gradient(ellipse at 50% 32%,var(--silver-1) 0 45%,var(--silver-2) 100%);
  }
  .mirror-word{
    position:absolute;top:300px;left:0;right:0;text-align:center;
    font-family:"Parisienne",cursive;color:var(--aqua);font-size:66px;
  }
  .subtitle{
    position:absolute;bottom:56px;left:0;right:0;text-align:center;
    font-family:"Raleway",sans-serif;font-weight:700;font-size:12.5px;letter-spacing:1.2px;color:var(--aqua-deep);
  }
  .front-author{
    position:absolute;bottom:0;left:0;right:0;height:44px;line-height:44px;text-align:center;
    font-family:"Raleway",sans-serif;font-weight:600;font-size:17px;letter-spacing:4px;color:var(--paper);
  }
</style>
</head>
<body>
<div class="spread">
  <section class="panel back">
    <div class="band-top"></div>
    <h2 class="back-title">The Shape of Stillness</h2>
    <p class="blurb">What does stillness really look like? Is it unreachable in the average teenage girl? How do teens find quiet in a world that measures worth by likes, looks and attention? Stillness carries an unpopular message in our culture, but the quietness of a steady heart has the power to shape a young woman's whole life. This book invites girls to see who they were made to be, to rest in that truth, and to grow a strength that does not need the crowd to cheer. It's time she learns that her heart was meant to bloom.</p>
    <div class="promise">
      <h3>THE SHAPE OF STILLNESS WILL:</h3>
      <ul>
        <li>Define what stillness is from God's view, and the world's.</li>
        <li>Teach girls about their true identity and purpose.</li>
        <li>Guide young women to build quiet strength each day.</li>
        <li>Name the common obstacles to a steady, peaceful life.</li>
        <li>Help girls grow a lifestyle of calm and courage.</li>
      </ul>
    </div>
    <div class="author-photo" role="img" aria-label="Author portrait photograph"></div>
    <div class="bio">
      <h4>COLETTE MERROW</h4>
      <p>Colette Merrow is a wife and mother of three living in the Midwest. She and her family first served in a small river town, where she led a home-based ministry for young women. She also writes music and enjoys mentoring. Her heart is to see girls from every background live in quiet strength. Learn more at www.colettemerrow.com.</p>
    </div>
    <div class="band-bottom"></div>
  </section>

  <section class="panel spine">
    <div class="band-top"></div>
    <div class="spine-text">
      <span class="spine-title">The Shape of Stillness</span>
      <span class="spine-author">COLETTE MERROW</span>
    </div>
    <div class="band-bottom"></div>
  </section>

  <section class="panel front">
    <div class="band-top"></div>
    <h1 class="front-title">
      <span class="small">The</span>
      <span class="large">Shape</span>
      <span class="mid">of</span>
    </h1>
    <div class="mirror" role="img" aria-label="Ornate silver hand mirror with aqua accents"></div>
    <div class="mirror-word">Stillness</div>
    <p class="subtitle">A YOUNG WOMAN'S MAP TO QUIET STRENGTH</p>
    <div class="band-bottom"></div>
    <p class="front-author">COLETTE MERROW</p>
  </section>
</div>
</body>
</html>
```